Take my 1-Page Consulting Service Introduction to the next level!

I am looking for a designer to enhance my current 1-Page Consulting Services Introduction.

My business - Bright Harbor Advisory - offers HR consulting to companies looking to be more people-centric. The design should be professional, but also convey a sense of "sparking people" or inspiring people to engage and excel.

The new Word document will:
* Use my new business logo, logo icon and colors. (files attached)
* Include my head shot (file attached)
* Impress potential clients by improving the visual appeal
* Be easy for me to update in Word (small edits)

Target Market(s)

Business owners and senior leaders

Font styles to use
Sans Serif

Requirements
Must have
• My head shot (can be cropped) , my logo
Nice to have
• use of my logo icon or parts of it (if that works for the design)

```html
<!DOCTYPE html>
<html lang="en">
<head>
<meta charset="utf-8">
<title>Dana Whitlock – Bright Harbor Advisory</title>
<link rel="stylesheet" href="https://fonts.googleapis.com/css2?family=Poppins:wght@400;600;700&family=Open+Sans:wght@400;600&display=swap">
<style>
  :root {
    --backdrop: #d8cfc1;
    --paper: #ffffff;
    --header-grey: #6b6b6b;
    --panel-grey: #6e6e6e;
    --light-step: #dadada;
    --dark-step: #2f2f2f;
    --ink: #3a3a3a;
    --ink-soft: #555555;
    --on-dark: #ffffff;
    --photo-top: #9aa3ad;
    --photo-bottom: #4a4f57;
  }
  * { box-sizing: border-box; margin: 0; padding: 0; }
  html, body { width: 1200px; height: 899px; overflow: hidden; }
  body {
    background: var(--backdrop);
    font-family: "Open Sans", Arial, sans-serif;
    color: var(--ink);
  }
  .flyer {
    position: absolute;
    left: 267px; top: 20px;
    width: 666px; height: 859px;
    background: var(--paper);
    box-shadow: 0 6px 18px rgba(0,0,0,.15);
    overflow: hidden;
  }
  .header-band {
    position: absolute; left: 0; top: 0;
    width: 100%; height: 320px;
    background: var(--header-grey);
  }
  .brand {
    position: absolute; left: 46px; top: 56px;
    display: flex; align-items: center; gap: 8px;
    font-family: "Poppins", Arial, sans-serif;
    font-weight: 600; font-size: 15px; line-height: 1.15;
    color: var(--on-dark);
  }
  .brand-dot { width: 12px; height: 12px; border-radius: 50%; background: var(--on-dark); flex: none; }
  .consultant-name {
    position: absolute; left: 46px; top: 150px;
    font-family: "Poppins", Arial, sans-serif;
    font-weight: 700; font-size: 38px;
    color: var(--on-dark);
  }
  .contact-box {
    position: absolute; left: 46px; top: 216px;
    width: 268px; padding: 10px 14px;
    border: 1px solid rgba(255,255,255,.8);
    list-style: none;
    font-size: 11px; color: var(--on-dark);
  }
  .contact-box li { display: flex; align-items: center; gap: 10px; line-height: 20px; }
  .contact-box svg { width: 11px; height: 11px; flex: none; fill: var(--on-dark); }
  .headshot {
    position: absolute; left: 400px; top: 22px;
    width: 238px; height: 238px; border-radius: 50%;
    border: 5px solid var(--paper);
    background: radial-gradient(circle at 50% 40%, var(--photo-top), var(--photo-bottom));
  }
  .intro {
    position: absolute; left: 46px; top: 342px; width: 580px;
    font-size: 10.5px; line-height: 1.5; color: var(--ink-soft);
  }
  .intro p + p { margin-top: 9px; }
  .services-panel {
    position: absolute; left: 46px; top: 476px;
    width: 256px; height: 250px;
    background: var(--panel-grey);
    padding: 16px 18px;
    list-style: none;
    color: var(--on-dark);
    font-size: 12px;
  }
  .services-panel li { line-height: 22.5px; }
  .services-panel li::before { content: "•"; margin-right: 8px; }
  .experience { position: absolute; left: 326px; top: 474px; width: 296px; }
  .section-title {
    font-family: "Poppins", Arial, sans-serif;
    font-weight: 700; font-size: 17px; color: var(--ink);
    margin-bottom: 6px;
  }
  .role-list { list-style: none; font-size: 10.5px; line-height: 1.4; color: var(--ink-soft); }
  .role-list li { padding-left: 12px; position: relative; }
  .role-list li::before { content: "•"; position: absolute; left: 0; }
  .credentials { margin-top: 14px; font-size: 10.5px; line-height: 1.45; color: var(--ink-soft); }
  .impact-arrow { position: absolute; left: 46px; top: 784px; width: 110px; height: 40px; }
  .impact-step {
    position: absolute; width: 132px; height: 62px;
    padding: 8px 10px;
    font-size: 8.5px; line-height: 1.35;
  }
  .impact-step.step-one { left: 180px; top: 784px; background: var(--panel-grey); color: var(--on-dark); }
  .impact-step.step-two { left: 312px; top: 752px; background: var(--light-step); color: var(--ink); }
  .impact-step.step-three { left: 444px; top: 720px; background: var(--dark-step); color: var(--on-dark); }
</style>
</head>
<body>
  <main class="flyer">
    <section class="header-band">
      <div class="brand"><span class="brand-dot"></span><span>Bright Harbor<br>Advisory</span></div>
      <h1 class="consultant-name">Dana Whitlock</h1>
      <ul class="contact-box">
        <li><svg viewBox="0 0 12 12"><path d="M6 0a4 4 0 0 0-4 4c0 3 4 8 4 8s4-5 4-8a4 4 0 0 0-4-4zm0 5.5A1.5 1.5 0 1 1 6 2.5a1.5 1.5 0 0 1 0 3z"/></svg>Kelowna, BC Canada</li>
        <li><svg viewBox="0 0 12 12"><path d="M2.5 0l2 3-1.2 1.3a7 7 0 0 0 4.4 4.4L9 7.5l3 2-1 2.3C5 12 0 7 .2 1z"/></svg>604.555.0142</li>
        <li><svg viewBox="0 0 12 12"><path d="M0 2h12v8H0zm1 1v.4l5 3.3 5-3.3V3z"/></svg>dwhitlock@brightharboradvisory.com</li>
      </ul>
      <div class="headshot" role="img" aria-label="Head shot of Dana Whitlock"></div>
    </section>

    <section class="intro">
      <p>Dana provides people strategy expertise that enables business growth and success. She's known for change, learning, culture and performance systems that engage and empower. Dana partners with boards and leadership teams to convert vision into action and thrives on kick-starting business initiatives. She is a champion of people-centric decision-making with a wide range of industry experience.</p>
      <p>Dana fosters cultures that create meaningful in-person, hybrid and virtual team connection. She has dual US and Canadian citizenship and works cross-border with ease. www.brightharboradvisory.com/dana</p>
    </section>

    <ul class="services-panel">
      <li>People Strategies &amp; Execution</li>
      <li>Business Transformation</li>
      <li>Change Leadership</li>
      <li>People Systems</li>
      <li>Leadership Development</li>
      <li>Personal &amp; Team Effectiveness</li>
      <li>Coaching</li>
      <li>Employee Engagement</li>
      <li>Learning &amp; Development</li>
      <li>People-Centric Outsourcing</li>
    </ul>

    <section class="experience">
      <h2 class="section-title">Professional Experience</h2>
      <ul class="role-list">
        <li>Vice President, Development &amp; Culture, Northfield Building Solutions</li>
        <li>Director, Restaurant Training &amp; Transformation Maple Grill Food Services of Canada</li>
        <li>Director of Education Coastal Real Estate Association</li>
        <li>Head of Virtual Communities Global Learning Network</li>
        <li>Director of Academic Technology Services Ridgeview College</li>
      </ul>
      <p class="credentials">Dana holds a Masters of Arts in Education and Human Development. She is a certified Lumen personal effectiveness coach, a certified Clearpath Assessments coach and an experienced Changewise Certified Change Practitioner.</p>
    </section>

    <svg class="impact-arrow" viewBox="0 0 110 40" aria-label="Impact">
      <polygon points="0,8 78,8 78,0 110,20 78,40 78,32 0,32" fill="var(--dark-step)"/>
      <text x="40" y="24.5" text-anchor="middle" fill="#fff" font-family="Poppins, Arial, sans-serif" font-weight="700" font-size="11">IMPACT</text>
    </svg>
    <div class="impact-step step-one">Creating people strategies that engage, inspire and enable organizational growth and success.</div>
    <div class="impact-step step-two">Creating people strategies that engage, inspire and enable organizational growth and success.</div>
    <div class="impact-step step-three">Creating people strategies that engage, inspire and enable organizational growth and success.</div>
  </main>
</body>
</html>
```